Creative Landscape Architecture Company Needs a Creative Business Card Design

Marsh and Partners, Inc. is a landscape architecture (LA) company started in 1997 in Austin, TX. We work on large commerical projects all around the U.S. and provide land planning, site planning, landscape design and architectural renderings.

We don't want this card to look like a LA firm's business card. We are looking for a business card design that is edgy and cool to reflect the more artistic and creative side of our company. We would like our clients to think "now there's a business card unlike any other LA that I've seen before."

We would like it to be in standard 2"x3.5" format. Double sided. Full color ok. Our company logo is attached. We like the logo but would not be adverse to any variations you would like to make to it. Feel free to change it up. Typically the logo has been a light saturated orange color but its not necessary that you stick with it.

Requirements
Must have
• 1. Company name
2. individuals name
3. email address
4. cell number
5. office number
6. website: www.marshandpartners-demo.net
7. Business address
Nice to have
• Can add (but not necessary)
Personal titles such as "president" or "registered landscape architect"

```html
<!DOCTYPE html>
<html lang="en">
<head>
<meta charset="utf-8">
<title>Marsh &amp; Partners – Business Card</title>
<link rel="stylesheet" href="https://fonts.googleapis.com/css2?family=Open+Sans:wght@400;600&display=swap">
<style>
  :root {
    --page: #ffffff;
    --card-deep: #1f4c93;
    --card-mid: #2a5ba6;
    --card-light: #3d73bf;
    --swoosh: #5a93d6;
    --swoosh-pale: #8fbbeb;
    --text: #ffffff;
    --text-soft: #e6eef9;
    --rule: rgba(255, 255, 255, 0.55);
    --emblem-top: #ffffff;
    --emblem-bottom: #dfe9f6;
  }
  * { margin: 0; padding: 0; box-sizing: border-box; }
  html, body {
    width: 1200px;
    height: 705px;
    overflow: hidden;
    background: var(--page);
    font-family: "Open Sans", sans-serif;
  }
  .card {
    position: absolute;
    left: 12px;
    top: 7px;
    width: 1172px;
    height: 690px;
    border-radius: 22px 110px 22px 110px;
    background: linear-gradient(160deg, var(--card-mid) 0%, var(--card-deep) 55%, var(--card-mid) 100%);
    overflow: hidden;
    color: var(--text);
  }
  .card__swoosh {
    position: absolute;
    left: 0;
    top: 0;
    width: 1172px;
    height: 690px;
  }
  .card__emblem {
    position: absolute;
    left: 60px;
    top: 84px;
    width: 348px;
    height: 538px;
    border-radius: 10px;
    background: linear-gradient(180deg, var(--emblem-top), var(--emblem-bottom));
  }
  .card__company {
    position: absolute;
    left: 461px;
    top: 86px;
    font-size: 70px;
    font-weight: 600;
    letter-spacing: 1px;
    line-height: 1;
    white-space: nowrap;
  }
  .card__rule {
    position: absolute;
    left: 461px;
    top: 196px;
    width: 668px;
    height: 2px;
    background: var(--rule);
  }
  .card__person {
    position: absolute;
    left: 461px;
    top: 230px;
    font-size: 36px;
    font-weight: 400;
    line-height: 1;
  }
  .contact {
    position: absolute;
    left: 461px;
    top: 304px;
    font-size: 25px;
    line-height: 60px;
    color: var(--text-soft);
  }
  .contact__row {
    display: grid;
    grid-template-columns: 112px 46px auto;
    align-items: start;
  }
  .contact__value--multi { line-height: 38px; padding-top: 11px; }
</style>
</head>
<body>
  <div class="card">
    <svg class="card__swoosh" viewBox="0 0 1172 690" aria-hidden="true">
      <path d="M0 560 C 260 600, 520 720, 1172 520 L1172 690 L0 690 Z" fill="var(--card-light)" opacity="0.55"/>
      <path d="M300 690 C 600 610, 900 560, 1172 470 L1172 500 C 900 600, 650 650, 420 690 Z" fill="var(--swoosh-pale)" opacity="0.35"/>
      <path d="M540 690 C 760 640, 980 600, 1172 560 L1172 690 Z" fill="var(--swoosh)" opacity="0.45"/>
      <path d="M700 120 C 900 60, 1060 40, 1172 30 L1172 0 L900 0 C 860 40, 780 90, 700 120 Z" fill="var(--swoosh)" opacity="0.18"/>
    </svg>

    <div class="card__emblem" role="img" aria-label="Company leaf emblem in white on a square panel"></div>

    <h1 class="card__company">MARSH &amp; PARTNERS</h1>
    <div class="card__rule"></div>
    <p class="card__person">Individuals name</p>

    <div class="contact">
      <div class="contact__row"><span>E-Mail</span><span>:</span><span>info@marshandpartners-demo.com</span></div>
      <div class="contact__row"><span>Mobile</span><span>:</span><span>555 010 4821</span></div>
      <div class="contact__row"><span>Phone</span><span>:</span><span>512.555.0147</span></div>
      <div class="contact__row"><span>Website</span><span>:</span><span>www.marshandpartners-demo.net</span></div>
      <div class="contact__row"><span>Address</span><span>:</span><span class="contact__value--multi">4410 Ridgeline Road, Suite 210<br>Austin, Texas 78731</span></div>
    </div>
  </div>
</body>
</html>
```